High end Coffee Roaster needs a Label design for new Blend

We are looking for a label design for a new blend called "Cold Brew Blend". It is a blend of coffee that we use for making cold brew coffee. The blend is sold as the whole bean and ground coffee in a bag as well as pre-brewed ready to drink in a bottle. We would like the label to be elegant but fun and It must include our logo. Please check out or website brightmillroasters.com or social media @brightmillroasters for information on our company and our coffees if you need more ideas on the kind of product we offer and our style.

Requirements
Must have
• Our Company Logo. Creative design.
Should not have
• This project should NOT be a corporate company logo, Please do NOT submit a design for a company logo this is a project for a Label. We already have a logo and we are looking for a design on a label. I have uploaded several examples of what we are looking for. Those examples are from other coffee companies who have cold brew. Those are examples only to give you a better idea of what im looking for. DO NOT COPY THEM.

```html
<!DOCTYPE html>
<html lang="en">
<head>
<meta charset="utf-8">
<title>Cold Brew Blend Label</title>
<link href="https://fonts.googleapis.com/css2?family=Montserrat:wght@400;600;800&family=Oswald:wght@300;600&display=swap" rel="stylesheet">
<style>
  :root {
    --stage: #222222;
    --paper: #ffffff;
    --photo-light: #eeeeee;
    --bean-dark: #2e1c14;
    --bean-mid: #5a3522;
    --panel-brown: #653e32;
    --accent-tan: #c8955a;
    --ink: #1f1a18;
    --brand-brown: #4b2e2a;
    --brand-gold: #f2b134;
  }
  * { margin: 0; padding: 0; box-sizing: border-box; }
  html, body { width: 1200px; height: 800px; overflow: hidden; }
  body { background: var(--stage); position: relative; }

  .label {
    position: absolute; left: 344px; top: 35px;
    width: 511px; height: 730px;
    background: var(--paper); overflow: hidden;
  }
  .label__hero {
    position: absolute; left: 0; top: 0; width: 511px; height: 593px;
    background: var(--photo-light); overflow: hidden;
  }
  .bean-pile {
    position: absolute; left: -6px; top: 49px; width: 476px; height: 476px;
    border-radius: 50%;
    background: radial-gradient(circle at 45% 45%, var(--bean-mid) 0%, var(--bean-dark) 70%, #3d2418 100%);
  }
  .title-panel {
    position: absolute; left: 102px; top: 127px; width: 409px; height: 355px;
    background: var(--panel-brown);
  }
  .title-panel__name {
    position: absolute; left: 27px; top: 20px;
    font-family: 'Montserrat', sans-serif; font-weight: 800;
    font-size: 96px; line-height: 83px; color: var(--paper);
    letter-spacing: 1px;
  }
  .title-panel__type {
    position: absolute; left: 29px; top: 274px;
    font-family: 'Montserrat', sans-serif; font-weight: 400;
    font-size: 38px; line-height: 38px; letter-spacing: 9px; color: var(--paper);
  }
  .title-panel__rule {
    position: absolute; left: 31px; top: 325px; width: 196px; height: 6px;
    background: var(--accent-tan);
  }

  .specs {
    position: absolute; left: 30px; top: 608px;
    font-family: 'Oswald', sans-serif; font-weight: 300;
    font-size: 14.5px; line-height: 19.5px; color: var(--ink);
    text-transform: uppercase;
  }
  .specs b { font-weight: 600; }

  .brand {
    position: absolute; left: 336px; top: 612px; width: 150px;
    display: flex; flex-direction: column; align-items: center;
  }
  .brand__dot {
    width: 48px; height: 48px; border-radius: 50%;
    background: var(--brand-gold); margin-bottom: 10px;
  }
  .brand__name {
    font-family: 'Montserrat', sans-serif; font-weight: 600;
    font-size: 15px; line-height: 18px; color: var(--brand-brown);
    text-align: center; letter-spacing: 0.5px;
  }
</style>
</head>
<body>
  <main class="label">
    <section class="label__hero">
      <div class="bean-pile" role="img" aria-label="Photograph of roasted coffee beans piled in a round heap"></div>
      <div class="title-panel">
        <h1 class="title-panel__name">COLD<br>BREW<br>BLEND</h1>
        <p class="title-panel__type">COFFEE</p>
        <div class="title-panel__rule"></div>
      </div>
    </section>

    <section class="specs">
      <p><b>Country</b> Ethiopia <b>Region</b> Multiple <b>Farm</b> Multiple</p>
      <p><b>Growing Elevation</b> 1,700 - 2,000 Meters</p>
      <p><b>Process</b> Wet Process <b>Roast Level</b> Full City</p>
      <p><b>Tasting Note</b> Rich Chocolate, Black Berry Syrup</p>
      <p><b>Net Wt 1</b>6 oz (145g)</p>
    </section>

    <div class="brand">
      <div class="brand__dot"></div>
      <p class="brand__name">BRIGHT MILL<br>ROASTERS</p>
    </div>
  </main>
</body>
</html>
```